" ELA NAO FOI ABERTA AINDA MAS SERA EM 20 DIAS. A VARTEMI - uma empresa especializada na prestação de serviços terceirizados integrados, auxiliando nossos clientes a reduzir custos indiretos, focar em seu negócio principal, sem se preocupar com serviços de apoio, como limpeza, copa, portaria, segurança, administrativo, zeladoria, telefonia e recepção. Uma empresa ou Condomínio apresenta necessidades diversas para se manter operando de maneira lucrativa e segura. Antes, cada negócio precisava atender às demandas por meio de sua infraestrutura interna. Mas uma opção vantajosa vem crescendo no mercado e merece destaque atualmente: a terceirização de atividades "

```html
<!DOCTYPE html>
<html lang="pt-BR">
<head>
<meta charset="UTF-8">
<title>VARTEMI — Papel Timbrado</title>
<link rel="stylesheet" href="https://fonts.googleapis.com/css2?family=Montserrat:wght@400;700&display=swap">
<style>
  :root {
    --backdrop: #e6e7ea;
    --paper: #ffffff;
    --paper-shade: #f1f2f4;
    --mark-tint: rgba(222, 224, 229, 1);
    --mark-fade: rgba(228, 230, 234, 0.6);
    --mark-clear: rgba(255, 255, 255, 0);
    --tab-fill: #eceef1;
    --brand-navy: #26335c;
    --footer-ink: #6d717a;
  }
  * { margin: 0; padding: 0; box-sizing: border-box; }
  html, body {
    width: 1200px;
    height: 1200px;
    overflow: hidden;
    background: var(--backdrop);
    font-family: "Montserrat", Arial, sans-serif;
  }
  .canvas {
    width: 1200px;
    height: 1200px;
    display: flex;
    align-items: center;
    justify-content: center;
  }
  .letterhead {
    position: relative;
    width: 778px;
    height: 1100px;
    background: linear-gradient(160deg, var(--paper) 0%, var(--paper) 45%, var(--paper-shade) 100%);
    box-shadow: 0 10px 30px rgba(0, 0, 0, 0.12);
    overflow: hidden;
  }
  .brand {
    position: absolute;
    top: 46px;
    left: 50%;
    transform: translateX(-50%);
    display: flex;
    align-items: center;
    gap: 10px;
  }
  .brand-square {
    width: 22px;
    height: 22px;
    background: var(--brand-navy);
  }
  .brand-name {
    font-weight: 700;
    font-size: 22px;
    letter-spacing: 3px;
    color: var(--brand-navy);
  }
  .brand-mark-area {
    position: absolute;
    left: -260px;
    top: 300px;
    width: 1000px;
    height: 860px;
    background: radial-gradient(closest-side at 50% 50%, var(--mark-tint) 0%, var(--mark-fade) 55%, var(--mark-clear) 100%);
  }
  .footer-tab {
    position: absolute;
    left: 0;
    bottom: 0;
    width: 778px;
    height: 40px;
  }
  .site-address {
    position: absolute;
    bottom: 52px;
    left: 0;
    width: 100%;
    text-align: center;
    font-size: 13px;
    color: var(--footer-ink);
    letter-spacing: 0.5px;
  }
</style>
</head>
<body>
<main class="canvas">
  <section class="letterhead">
    <header class="brand">
      <span class="brand-square"></span>
      <span class="brand-name">VARTEMI</span>
    </header>

    <div class="brand-mark-area" role="img" aria-label="Marca da empresa em grande escala, aplicada em tom cinza claro como fundo decorativo"></div>

    <footer class="site-address">www.vartemi.com.br</footer>

    <svg class="footer-tab" viewBox="0 0 778 40" preserveAspectRatio="none" aria-hidden="true">
      <path d="M260 40 Q268 8 310 8 L468 8 Q510 8 518 40 Z" fill="var(--tab-fill)"/>
    </svg>
  </section>
</main>
</body>
</html>
```